Aesthetics Company Flyer (description of services)

We need a 5.5"x8.5" flyer describing the services we offer at radiant meadowbrook aesthetics. We are an aesthetics company located in Conroe TX. Our products and services can be found at www.rmaesthetica.example/services . We would like to see designs that are cohesive with our brand and website: https://www.rmaesthetica.example/

```html
<!DOCTYPE html>
<html lang="en">
<head>
<meta charset="UTF-8">
<title>Radiant Meadowbrook Aesthetics – Our Services</title>
<link rel="stylesheet" href="https://fonts.googleapis.com/css2?family=Cinzel:wght@400;600;700&family=Lora:wght@400&display=swap">
<style>
  :root {
    --page-bg: #e6e6e6;
    --paper: #ffffff;
    --lavender: #b19ccf;
    --lavender-soft: #c9b9e0;
    --plum: #4b3a60;
    --plum-deep: #2f2540;
    --ink: #2a2a2a;
    --tile-veil: rgba(255, 255, 255, 0.78);
  }
  * { box-sizing: border-box; margin: 0; padding: 0; }
  html, body {
    width: 1200px; height: 900px; overflow: hidden;
    background: var(--page-bg);
  }
  .flyer {
    position: absolute; left: 325px; top: 25px;
    width: 550px; height: 850px;
    background: var(--paper);
    overflow: hidden;
    box-shadow: 0 8px 24px rgba(0,0,0,0.12);
  }
  .hero {
    position: absolute; left: 0; top: 0; width: 550px; height: 305px;
    background: linear-gradient(90deg, #1d1a22 0%, #3a2c44 45%, var(--plum) 75%, #5d4a74 100%);
  }
  .hero-photo {
    position: absolute; left: 0; top: 0; width: 360px; height: 305px;
    background: radial-gradient(ellipse at 35% 45%, #c48f6e 0%, #8a5a45 35%, #3a2a33 70%, rgba(58,42,68,0) 100%);
  }
  .brand-box {
    position: absolute; right: 22px; top: 95px;
    width: 100px; height: 100px; background: var(--paper);
    display: flex; flex-direction: column; align-items: center; justify-content: center; gap: 6px;
    padding: 8px;
  }
  .brand-dot { width: 26px; height: 26px; border-radius: 50%; background: var(--lavender); }
  .brand-name {
    font-family: "Cinzel", serif; font-weight: 600; font-size: 9px; line-height: 1.25;
    color: var(--plum); text-align: center; letter-spacing: 0.5px;
  }
  .tagline {
    position: absolute; right: 22px; top: 210px;
    font-family: "Cinzel", serif; font-weight: 400; font-size: 17px; line-height: 1.15;
    color: #fff; text-align: right; letter-spacing: 0.5px;
  }
  .services-rule {
    position: absolute; left: 0; top: 318px; width: 550px; height: 2px; background: var(--lavender);
  }
  .services-banner {
    position: absolute; left: 28px; top: 292px; width: 300px; height: 52px;
    background: var(--lavender); border-radius: 10px;
    display: flex; align-items: center; justify-content: center;
    font-family: "Cinzel", serif; font-weight: 700; font-size: 25px; color: #fff; letter-spacing: 1px;
  }
  .service { position: absolute; width: 150px; }
  .service-photo { position: relative; width: 150px; height: 150px; }
  .service-text {
    position: absolute; left: 18px; top: 18px; right: 18px; bottom: 18px;
    background: var(--tile-veil);
    font-family: "Lora", serif; font-size: 8px; line-height: 1.35; color: var(--ink);
    padding: 10px 8px; text-align: center;
  }
  .service-name {
    margin-top: 6px;
    font-family: "Cinzel", serif; font-weight: 700; font-size: 10.5px; line-height: 1.2;
    color: var(--ink); text-align: center;
  }
  .col-1 { left: 25px; }
  .col-2 { left: 200px; }
  .col-3 { left: 375px; }
  .tone-warm   { background: linear-gradient(135deg, #e0a36b, #c9875c 50%, #f1e3d4); }
  .tone-grey   { background: linear-gradient(135deg, #cfcfcf, #8e8e8e 60%, #e8e8e8); }
  .tone-blue   { background: linear-gradient(135deg, #2a9fd6, #d8b8a4 55%, #f0dcd0); }
  .tone-pale   { background: linear-gradient(135deg, #ece7e4, #c2b7b1 60%, #f4f0ee); }
  .tone-peach  { background: linear-gradient(135deg, #e9b89a, #b98a77 55%, #6c7fa8); }
  .tone-gold   { background: linear-gradient(135deg, #555, #e5c450 45%, #9a9a9a); }
  .footer {
    position: absolute; left: 0; bottom: 0; width: 550px; height: 62px;
    background: var(--lavender);
    display: flex; align-items: center; justify-content: space-around;
    font-family: "Lora", serif; font-size: 12px; color: #fff;
  }
  .contact { display: flex; align-items: center; gap: 7px; }
  .contact svg { width: 14px; height: 14px; }
</style>
</head>
<body>
<main class="flyer">
  <section class="hero">
    <div class="hero-photo" role="img" aria-label="Portrait photograph of two women with glowing skin"></div>
    <div class="brand-box">
      <span class="brand-dot"></span>
      <span class="brand-name">Radiant Meadowbrook Aesthetics</span>
    </div>
    <h2 class="tagline">We change<br>the world<br>one beautiful<br>face at a time</h2>
  </section>

  <div class="services-rule"></div>
  <h1 class="services-banner">Our Services</h1>

  <article class="service col-1" style="top:370px">
    <div class="service-photo tone-warm" role="img" aria-label="Photo of a weight loss consultation">
      <p class="service-text">Medically guided weight loss programs built around you, with steady support and safe options to help reach your goals.</p>
    </div>
    <h3 class="service-name">Weightloss</h3>
  </article>
  <article class="service col-1" style="top:565px">
    <div class="service-photo tone-pale" role="img" aria-label="Photo of a fibrin growth factor skin treatment">
      <p class="service-text">Uses growth factors drawn from your own blood to boost collagen, improve texture and renew tired skin.</p>
    </div>
    <h3 class="service-name">Fibrin Growth Factor (FGF)</h3>
  </article>

  <article class="service col-2" style="top:395px">
    <div class="service-photo tone-grey" role="img" aria-label="Photo of a wrinkle relaxer injection">
      <p class="service-text">Softens lines around the eyes and brow by relaxing the muscles beneath, giving the skin a smooth, rested appearance.</p>
    </div>
    <h3 class="service-name">Neurotoxin (Wrinkle Relaxer)</h3>
  </article>
  <article class="service col-2" style="top:595px">
    <div class="service-photo tone-peach" role="img" aria-label="Photo of a microneedling treatment">
      <p class="service-text">Fine needling that triggers natural repair to soften scars, fine lines and enlarged pores with little downtime.</p>
    </div>
    <h3 class="service-name">Microneedling</h3>
  </article>

  <article class="service col-3" style="top:420px">
    <div class="service-photo tone-blue" role="img" aria-label="Photo of a dermal filler treatment with gloved hands">
      <p class="service-text">Restores lost volume to lips and cheeks and smooths deep folds for a natural, refreshed look that lasts.</p>
    </div>
    <h3 class="service-name">Dermal Fillers</h3>
  </article>
  <article class="service col-3" style="top:600px">
    <div class="service-photo tone-gold" role="img" aria-label="Photo of a chemical peel mask being applied">
      <p class="service-text">Lifts dull outer layers to reveal brighter, even skin tone.</p>
    </div>
    <h3 class="service-name">Chemical Peels</h3>
  </article>

  <footer class="footer">
    <span class="contact">
      <svg viewBox="0 0 14 14" aria-hidden="true"><circle cx="7" cy="7" r="6" fill="none" stroke="#fff" stroke-width="1.2"/><ellipse cx="7" cy="7" rx="2.6" ry="6" fill="none" stroke="#fff" stroke-width="1"/><line x1="1" y1="7" x2="13" y2="7" stroke="#fff" stroke-width="1"/></svg>
      www.rmaesthetica.example
    </span>
    <span class="contact">
      <svg viewBox="0 0 14 14" aria-hidden="true"><rect x="1" y="3" width="12" height="8" fill="none" stroke="#fff" stroke-width="1.2"/><polyline points="1,3 7,8 13,3" fill="none" stroke="#fff" stroke-width="1.2"/></svg>
      hello@rmaesthetica.example
    </span>
    <span class="contact">
      <svg viewBox="0 0 14 14" aria-hidden="true"><path d="M3 1.5 L5.5 1.5 L6.5 4.5 L5 5.8 C5.8 7.6 6.6 8.4 8.2 9.2 L9.5 7.6 L12.5 8.6 L12.5 11.2 C12.5 12 11.8 12.6 11 12.5 C5.6 12 2 8.4 1.5 3 C1.4 2.2 2.1 1.5 3 1.5 Z" fill="#fff"/></svg>
      936 555 0142
    </span>
  </footer>
</main>
</body>
</html>
```